I have a logo and need to design the business card and stationery.
Updates

The uploaded logo image named as GREYHAVEN CONSTRUCTION which is to be replaced to GREYHAVEN CONTRACTS. Kindly add below details and submit the designs- Company name- Greyhaven Engineering Contracts LLP Name & Post- Kunal Mehra (Designated Partner) Address- Block No.317, Wing C, Tulsi Trade Plaza, Lokhand Marg, Varun Industrial Park, Goregaon(E), Mumbai - 400 063 Contact- +91 97410 58723 Email- kunalmehra@examplemail.com Website- www.greyhavencontracts.example Contact for Letterhead- +91-22-28145597

Hi Tanvir Rahman, We are liking your Design #41927506. We have suggested some changes which are mentioned in feedback. Kindly revert with it asap to finalize this design.

Colors

Designer to choose colors to be used in the design.

```html
<!DOCTYPE html>
<html lang="en">
<head>
<meta charset="utf-8">
<title>Greyhaven Contracts — Business Card</title>
<link href="https://fonts.googleapis.com/css2?family=Ubuntu:wght@400;500;700&display=swap" rel="stylesheet">
<style>
  :root{
    --bg:#9a9a9a;
    --card-white:#ffffff;
    --charcoal:#333333;
    --ink-light:#ffffff;
    --emboss:#6e6e6e;
  }
  *{margin:0;padding:0;box-sizing:border-box}
  html,body{width:1133px;height:1200px;overflow:hidden;background:var(--bg);font-family:'Ubuntu',sans-serif}
  .card{position:absolute;width:734px;height:417px}
  .card--front{left:192px;top:139px;background:var(--card-white)}
  .card--back{left:196px;top:641px;background:var(--charcoal)}

  .info-panel{position:absolute;left:16px;top:15px;width:313px;height:389px;background:var(--charcoal);color:var(--ink-light)}
  .person-name{position:absolute;left:32px;top:90px;font-size:25px;font-weight:700;letter-spacing:.3px}
  .person-role{position:absolute;left:32px;top:120px;font-size:16px}
  .address{position:absolute;left:34px;top:164px;font-size:17px;line-height:21px}
  .contact-list{position:absolute;left:34px;top:239px;list-style:none;font-size:17px;line-height:21px}
  .contact-list li{display:flex;align-items:center;gap:8px}
  .contact-list svg{width:15px;height:15px;fill:var(--ink-light);flex:none}

  .brand-block{position:absolute;left:329px;top:15px;width:581px;height:389px}
  .brand-front{position:absolute;left:150px;top:55px;display:flex;flex-direction:column;align-items:center;gap:22px;width:280px}
  .brand-square{width:150px;height:150px;background:var(--charcoal)}
  .brand-name{font-size:26px;font-weight:700;color:var(--charcoal);text-align:center;line-height:32px;letter-spacing:2px}

  .brand-back{position:absolute;left:0;top:119px;width:100%;display:flex;flex-direction:column;align-items:center;gap:20px}
  .brand-back .brand-square{width:106px;height:106px;background:none;border:6px solid var(--emboss)}
  .brand-back .brand-name{color:var(--emboss);font-size:30px;letter-spacing:3px;line-height:30px}
</style>
</head>
<body>
  <section class="card card--front">
    <div class="info-panel">
      <h1 class="person-name">DANIEL HARPER</h1>
      <p class="person-role">President</p>
      <address class="address" style="font-style:normal">4120 Willowbrook Lane<br>Fairbanks<br>Alaska 99712</address>
      <ul class="contact-list">
        <li><svg viewBox="0 0 24 24"><path d="M6.6 10.8a15 15 0 0 0 6.6 6.6l2.2-2.2c.3-.3.7-.4 1-.2 1.1.4 2.3.6 3.6.6.6 0 1 .4 1 1V20c0 .6-.4 1-1 1A17 17 0 0 1 3 4c0-.6.4-1 1-1h3.5c.6 0 1 .4 1 1 0 1.3.2 2.5.6 3.6.1.3 0 .7-.2 1z"/></svg>907-438-2716</li>
        <li><svg viewBox="0 0 24 24"><path d="M7 1h10a2 2 0 0 1 2 2v18a2 2 0 0 1-2 2H7a2 2 0 0 1-2-2V3a2 2 0 0 1 2-2zm0 3v14h10V4z"/></svg>907-621-5093</li>
        <li><svg viewBox="0 0 24 24"><path d="M2 5h20v14H2zm2 2v1l8 5 8-5V7l-8 5z"/></svg>name@greyhaven.example</li>
        <li><svg viewBox="0 0 24 24"><path d="M12 2a10 10 0 1 0 0 20 10 10 0 0 0 0-20zm-1 17.9A8 8 0 0 1 4.2 10L9 15v1a2 2 0 0 0 2 2zm6.9-2.5A2 2 0 0 0 16 16h-1v-3a1 1 0 0 0-1-1H8v-2h2a1 1 0 0 0 1-1V7h2a2 2 0 0 0 2-2v-.4a8 8 0 0 1 2.9 12.8z"/></svg>www.greyhaven.example</li>
      </ul>
    </div>
    <div class="brand-block">
      <div class="brand-front">
        <div class="brand-square"></div>
        <p class="brand-name">GREYHAVEN<br>CONTRACTS</p>
      </div>
    </div>
  </section>

  <section class="card card--back">
    <div class="brand-back">
      <div class="brand-square"></div>
      <p class="brand-name">GREYHAVEN<br>CONTRACTS</p>
    </div>
  </section>
</body>
</html>
```